Web Site Design for a Finance (lending) Company

We are opening a new subsidiary that focuses on lending money in the real estate industry. We need a web site designed to represent the business.

The business is lending money to real estate investors. A typical client/borrower will be looking to borrow money to buy a house, renovate it and then sell it at a profit, all within 12 months or less.

Company name is Brevand Finance. Our logo is attached.

Attached is a general outline for the web site. We're working on writing more text for each page but this should give you enough to get started with some ideas.

Competitor web site that I like a lot (as an example): https://quorvelfunding.com/. Many of the general items on this site match what we will need (description of loan programs, FAQ)

Target Market(s)

Real estate investors (generally individuals or small companies with just a few people) who are buying homes, renovating them and then selling them at a profit.

Industry/Entity Type

Finance

Coding

Coded - Design and coding required

Number of Pages Required

5+ page

Colors

Designer to choose colors to be used in the design.

Requirements
Must have
• Minimalist design. Clean lines without too much clutter. Some stock photography is ok but the photos should not be distracting. They should almost fade in to the background so that user can focus on the key information about what our company does instead. We are a finance company, not a design company, so the information about our products will be more interesting to site visitors than the art.
• Some minimalist examples from Snapboard:
• https://www.snapboard-example.com/explore/minimalist-web-design/
Nice to have
• If you search in seekly for "hard money lenders" you will find many examples of web sites from our competition. I have provided a link above to competitor web site that I like a lot.
• I have attached our logo in EPS format. Logo is green. Web site doesn't have to be green but it should be of a color that will work well with the logo.

```html
<!DOCTYPE html>
<html lang="en">
<head>
<meta charset="utf-8">
<title>Brevand Finance</title>
<link href="https://fonts.googleapis.com/css2?family=Open+Sans:wght@400;600;700&display=swap" rel="stylesheet">
<style>
:root{
  --green:#0c4b2f;
  --green-dark:#083a24;
  --ink:#2d2d2d;
  --muted:#7a7a7a;
  --line:#dcdcdc;
  --light:#f2f2f2;
  --footer:#353535;
  --chat:#f4a81d;
  --white:#fff;
}
*{box-sizing:border-box;margin:0;padding:0}
html,body{width:1200px;height:3040px;overflow:hidden}
body{font-family:"Open Sans",Arial,sans-serif;color:var(--ink);background:var(--white);position:relative}
.site-header{height:132px;position:relative}
.brand{position:absolute;left:120px;top:34px;display:flex;align-items:center;gap:14px}
.brand-mark{width:44px;height:44px;background:var(--green)}
.brand-name{font-size:30px;font-weight:700;color:var(--green);line-height:1}
.header-contact{position:absolute;right:128px;top:22px;display:flex;align-items:center;gap:14px;font-size:20px;font-weight:700}
.header-contact svg{width:18px;height:18px}
.login{border:1px solid var(--ink);font-size:13px;padding:2px 8px;font-weight:400}
.main-nav{position:absolute;right:120px;top:88px;display:flex;gap:34px;font-size:15px}
.main-nav a{color:var(--ink);text-decoration:none}
.main-nav a.active{border-bottom:2px solid var(--ink)}
.hero{height:468px;background:linear-gradient(180deg,#5c7a9a 0%,#8a8a7a 45%,#5a4a36 75%,#3b4a2a 100%)}
.intro{height:600px;position:relative;border-bottom:1px solid var(--line)}
.intro-text{position:absolute;left:130px;top:86px;width:510px}
.intro-text h1{font-size:26px;font-weight:700;color:var(--green);line-height:1.3;margin-bottom:22px}
.intro-text ul{list-style:none;font-size:13px;color:var(--muted);line-height:1.55}
.intro-text li{position:relative;padding-left:16px;margin-bottom:8px}
.intro-text li::before{content:"";position:absolute;left:0;top:8px;width:5px;height:5px;border-radius:50%;background:var(--muted)}
.btn{display:inline-block;background:var(--green);color:var(--white);font-size:13px;padding:10px 16px;border-radius:3px;text-decoration:none}
.intro .btn{margin-top:32px}
.intro-photo{position:absolute;left:736px;top:88px;width:334px;height:316px;background:linear-gradient(160deg,#9bb6d8 0%,#c9c2b6 45%,#7a5a44 100%)}
.loans{height:432px;background:var(--green);position:relative}
.section-title{text-align:center;font-size:26px;font-weight:600}
.loans .section-title{color:var(--white);padding-top:56px;display:flex;justify-content:center;align-items:center;gap:10px}
.loans .section-title svg{width:36px;height:36px}
.loan-cards{position:absolute;top:130px;left:130px;right:130px;display:flex;justify-content:space-between}
.loan-card{width:450px;height:248px;background:var(--white);padding:24px 34px}
.loan-card svg{width:26px;height:26px;display:block}
.loan-card h2{font-size:22px;font-weight:600;margin:6px 0 10px;white-space:nowrap;line-height:1.3}
.loan-card ul{list-style:none;font-size:12px;color:var(--muted);line-height:1.7}
.loan-card li::before{content:"• "}
.btn-ghost{display:inline-block;border:1px solid var(--line);font-size:11px;color:var(--muted);padding:6px 14px;margin-top:14px;border-radius:3px}
.resources{height:778px;position:relative;border-bottom:1px solid var(--line)}
.resources .section-title{padding-top:80px}
.resource-cards{position:absolute;top:122px;left:130px;right:130px;display:flex;justify-content:space-between}
.resource-card{width:304px;height:430px;background:var(--light)}
.resource-photo{height:186px}
.photo-a{background:linear-gradient(170deg,#a9c4e4 0%,#b0785a 55%,#5d7a3c 100%)}
.photo-b{background:linear-gradient(170deg,#6f93c4 0%,#9aa4ae 55%,#4a5560 100%)}
.photo-c{background:linear-gradient(170deg,#d6dde4 0%,#f3f3f3 55%,#8a8e88 100%)}
.resource-body{padding:22px 20px}
.resource-body h3{font-size:15px;font-weight:400;line-height:1.35;margin-bottom:12px}
.resource-body p{font-size:11px;color:var(--muted);line-height:1.6}
.more{position:absolute;left:50%;transform:translateX(-50%);top:590px;border:1px solid var(--line);font-size:11px;color:var(--muted);padding:6px 14px;border-radius:3px}
.membership{height:190px;border-bottom:1px solid var(--line)}
.membership .section-title{color:var(--green);padding-top:42px;font-size:24px}
.member-list{display:flex;justify-content:space-between;align-items:center;padding:34px 130px 0}
.member{font-size:17px;font-weight:700;color:var(--ink)}
.contact{height:336px;background:var(--light);position:relative}
.contact .section-title{color:var(--green);padding-top:60px;font-size:24px}
.contact-form{position:absolute;left:130px;right:130px;top:116px}
.form-row{display:flex;gap:18px;margin-bottom:16px}
.field{flex:1;height:32px;background:var(--white);border:1px solid var(--line);font-size:11px;color:var(--muted);padding:8px 10px}
.field-message{height:40px}
.contact .btn{position:absolute;left:50%;transform:translateX(-50%);top:252px;padding:8px 14px;font-size:12px}
.site-footer{position:absolute;top:2936px;left:0;width:1200px;height:104px;background:var(--footer);color:#bbb;font-size:11px}
.footer-links{position:absolute;left:130px;top:28px;display:flex;gap:18px}
.copyright{position:absolute;left:130px;top:52px;color:#999}
.social{position:absolute;right:130px;top:34px;display:flex;gap:8px}
.social span{width:22px;height:22px;border-radius:50%;background:#3d7bbf}
.chat{position:absolute;left:728px;top:2744px;width:222px;height:296px;background:var(--white);border:1px solid var(--line);box-shadow:0 2px 8px rgba(0,0,0,.2)}
.chat-head{background:var(--chat);color:var(--white);font-size:12px;font-weight:600;padding:9px 12px}
.chat-body{padding:12px}
.chat .field{display:block;height:26px;margin-bottom:10px;font-size:10px;padding:5px 8px}
.chat .chat-msg{height:60px}
.chat-send{display:inline-block;background:var(--footer);color:var(--white);font-size:10px;padding:5px 10px}
</style>
</head>
<body>
<header class="site-header">
  <div class="brand"><span class="brand-mark"></span><span class="brand-name">Brevand Finance</span></div>
  <div class="header-contact">
    <svg viewBox="0 0 24 24" aria-hidden="true"><path fill="#2d2d2d" d="M6.6 10.8a15 15 0 0 0 6.6 6.6l2.2-2.2a1 1 0 0 1 1-.25 11.4 11.4 0 0 0 3.6.57 1 1 0 0 1 1 1V20a1 1 0 0 1-1 1A17 17 0 0 1 3 4a1 1 0 0 1 1-1h3.5a1 1 0 0 1 1 1 11.4 11.4 0 0 0 .57 3.6 1 1 0 0 1-.25 1z"/></svg>
    <span>555 318 2047</span><span class="login">Login</span>
  </div>
  <nav class="main-nav"><a class="active" href="#">Home</a><a href="#">About Us</a><a href="#">Loans</a><a href="#">Resources</a><a href="#">Contact Us</a></nav>
</header>

<div class="hero" role="img" aria-label="Modern two-storey house lit at dusk with a paved driveway"></div>

<section class="intro">
  <div class="intro-text">
    <h1>Local real estate experts lending to local real estate investors</h1>
    <ul>
      <li>Brevand Finance is a local business with local knowledge and strong industry relationships to partner with a wide network that offers value added services.</li>
      <li>It is led by an established panel of experienced investors available for your real estate investment needs.</li>
      <li>Loans offered: Fix and Flip, Commercial.</li>
      <li>Why borrow from Brevand? Fast approval, professional service, a painless process, education, competitive rates and fees.</li>
    </ul>
    <a class="btn" href="#">Apply Now</a>
  </div>
  <div class="intro-photo" role="img" aria-label="House under renovation with new roof and scaffolding"></div>
</section>

<section class="loans">
  <h2 class="section-title">
    <svg viewBox="0 0 36 36" aria-hidden="true"><circle cx="18" cy="11" r="7" fill="none" stroke="#fff" stroke-width="2"/><path d="M4 26h8l6 3h9l5-4" fill="none" stroke="#fff" stroke-width="2"/></svg>Loans
  </h2>
  <div class="loan-cards">
    <article class="loan-card">
      <svg viewBox="0 0 24 24" aria-hidden="true"><path fill="#0c4b2f" d="M12 3 2 12h3v8h5v-5h4v5h5v-8h3z"/></svg>
      <h2>Fix and Flip Loans</h2>
      <ul><li>Description of the loan type, borrower requirements</li><li>Loan terms table (rate, loan to cost etc.)</li><li>Why choose Brevand</li><li>Online application or Contact web form</li></ul>
      <span class="btn-ghost">Read more</span>
    </article>
    <article class="loan-card">
      <svg viewBox="0 0 24 24" aria-hidden="true"><path fill="#0c4b2f" d="M5 2h14v20h-5v-4h-4v4H5zm3 3v2h2V5zm6 0v2h2V5zM8 9v2h2V9zm6 0v2h2V9zM8 13v2h2v-2zm6 0v2h2v-2z"/></svg>
      <h2>Commercial Hard Money Loans</h2>
      <ul><li>Description of the loan type, borrower requirements</li><li>Loan terms table (rate, loan to cost etc.)</li><li>Why choose Brevand</li><li>Online application or Contact web form</li></ul>
      <span class="btn-ghost">Read more</span>
    </article>
  </div>
</section>

<section class="resources">
  <h2 class="section-title">Resources</h2>
  <div class="resource-cards">
    <article class="resource-card">
      <div class="resource-photo photo-a" role="img" aria-label="Brick family house with front lawn"></div>
      <div class="resource-body"><h3>Fusce sollicitudin lorem et luctus aliquet</h3><p>Maecenas consequat justo enim, ut mattis massa nec. Fusce eget nunc ullamcorper, tincidunt et magna congue, dictum vehicula nisl.</p><span class="btn-ghost">Read more</span></div>
    </article>
    <article class="resource-card">
      <div class="resource-photo photo-b" role="img" aria-label="Glass office towers under a blue sky"></div>
      <div class="resource-body"><h3>Pellentesque a imperdiet dolor, et auctor est</h3><p>Maecenas consequat justo enim, ut mattis massa nec. Fusce eget nunc ullamcorper, tincidunt et magna congue, dictum vehicula nisl.</p><span class="btn-ghost">Read more</span></div>
    </article>
    <article class="resource-card">
      <div class="resource-photo photo-c" role="img" aria-label="White modern villa with flat roof"></div>
      <div class="resource-body"><h3>Pellentesque convallis molestie enim sit amet efficitur</h3><p>Maecenas consequat justo enim, ut mattis massa nec. Fusce eget nunc ullamcorper, tincidunt et magna congue, dictum vehicula nisl.</p><span class="btn-ghost">Read more</span></div>
    </article>
  </div>
  <span class="more">View all</span>
</section>

<section class="membership">
  <h2 class="section-title">Industry Membership</h2>
  <div class="member-list">
    <span class="member">Corvia</span><span class="member">Tandel</span><span class="member">Wavecrest</span><span class="member">Oakmere</span><span class="member">Ferrow</span><span class="member">Lumio</span><span class="member">Stonefield</span>
  </div>
</section>

<section class="contact">
  <h2 class="section-title">Contact Us</h2>
  <div class="contact-form">
    <div class="form-row"><span class="field">Name</span><span class="field">Email</span><span class="field">Phone</span><span class="field">City</span></div>
    <div class="form-row"><span class="field field-message">Message</span></div>
  </div>
  <a class="btn" href="#">Submit</a>
</section>

<footer class="site-footer">
  <div class="footer-links"><span>Home</span><span>About Us</span><span>Loans</span><span>Resources</span><span>Contact Us</span></div>
  <div class="copyright">Copyright © 2017 Brevand Finance. All rights reserved.</div>
  <div class="social"><span></span><span></span><span></span></div>
</footer>

<aside class="chat">
  <div class="chat-head">Live Chat with us</div>
  <div class="chat-body">
    <span class="field">Name</span>
    <span class="field">Email</span>
    <span class="field chat-msg">Message</span>
    <span class="chat-send">Leave</span>
  </div>
</aside>
</body>
</html>
```